CBD PATCHES

Design creation of my CBD patch box.
Product must look Pharamaceutical grade.
Colours need to look pharmaceutical (green/white/maybe a bit of blue).
Text: Cannabidiol (CBD) Self-curing adhesive Polyethylene backing sheet.
Apply one patch to a smooth are of skin. Each patch can be worn for up to 24 hours. Apply subsequent patches to different areas to allow the skin to breathe between uses.
Do not apply to broken or irritable skin. Consult a doctor if you are taking medications or have medical conditions before using this or any other supplement. Do not use if you are pregnant or breastfeeding.
Store in a cool, dry place out of direct sunlight. Stable for three years. Once opened, use within 12 months.

```html
<!DOCTYPE html>
<html lang="en">
<head>
<meta charset="utf-8">
<title>CBD Patch Box – Flat Panels</title>
<link rel="stylesheet" href="https://fonts.googleapis.com/css2?family=Outfit:wght@400;500;700&display=swap">
<style>
  :root {
    --green: #8aa84a;
    --green-light: #a6c261;
    --green-shadow: #dfe8cf;
    --blue: #1f6fa0;
    --ink: #1d1d1b;
    --panel: #ffffff;
    --line: #2b2b2b;
    --page: #ffffff;
  }
  * { margin: 0; padding: 0; box-sizing: border-box; }
  html, body { width: 1200px; height: 1000px; overflow: hidden; background: var(--page); }
  body { position: relative; font-family: "Outfit", sans-serif; color: var(--ink); }

  .dieline { position: absolute; top: 0; width: 566px; height: 1000px; }
  .dieline--back { left: 22px; }
  .dieline--front { left: 612px; }
  .dieline-art { position: absolute; left: 0; top: 0; width: 100%; height: 100%; }
  .dieline-art .cut { fill: var(--panel); stroke: var(--line); stroke-width: 0.6; }
  .dieline-art .fold { fill: none; stroke: var(--line); stroke-width: 0.6; }

  .face {
    position: absolute; left: 123px; top: 189px; width: 321px; height: 335px;
    overflow: hidden; background: var(--panel);
  }

  /* back panel */
  .face--info { padding: 24px 26px 0 22px; font-size: 12.4px; line-height: 1.38; }
  .face--info p { margin-bottom: 14px; }
  .face--info .label { color: var(--green); font-weight: 500; }
  .storage {
    margin-top: 2px; background: var(--green); color: #fff; text-align: center;
    border-radius: 14px; padding: 9px 12px; font-size: 12px; line-height: 1.32;
    box-shadow: -3px 4px 0 var(--green-shadow);
  }

  /* front panel */
  .face--front .brand {
    position: absolute; left: 24px; top: 22px; display: flex; align-items: center; gap: 6px;
    color: var(--green-light); font-weight: 500; font-size: 10px; letter-spacing: 0.12em;
  }
  .face--front .brand-dot { width: 14px; height: 14px; border-radius: 50%; background: var(--green-light); }
  .face--front .product {
    position: absolute; left: 24px; top: 128px; color: var(--green);
    font-weight: 700; font-size: 31px; line-height: 1.12; z-index: 1;
  }
  .face--front .spec {
    position: absolute; left: 24px; top: 220px; color: var(--blue);
    font-weight: 400; font-size: 14.5px; line-height: 1.32; z-index: 1;
  }
  .face--front .arc {
    position: absolute; right: 0; top: 100px; width: 62px; height: 200px;
  }
</style>
</head>
<body>

<section class="dieline dieline--back" aria-label="Back panel">
  <svg class="dieline-art" viewBox="0 0 300 530" preserveAspectRatio="none" aria-hidden="true">
    <path class="cut" d="M65 30 H115 C115 10 125 5 150 5 C175 5 185 10 185 30 H235 V278
      H258 C285 278 297 292 297 318 V445 H235 L225 445 Q222 448 222 455 V525 H175 C175 505 165 495 150 495 C135 495 125 505 125 525 H78 V455 Q78 448 75 445 H65
      H2 V318 C2 292 14 278 41 278 H65 Z"/>
    <path class="fold" d="M65 100 H235 M65 365 H235 M65 278 V445 M235 278 V445 M116 388 L118 392 H182 L184 388 M20 345 L37 362 M280 345 L263 362"/>
  </svg>
  <div class="face face--info">
    <p><span class="label">Direction:</span> Apply one patch to a smooth are of skin. Each patch can be worn for up to 24 hours. Apply subsequent patches to different areas to allow the skin to breathe between uses.</p>
    <p><span class="label">Description:</span> Do not apply to broken or irritable skin. Consult a doctor if you are taking medications or have medical conditions before using this or any other supplement. Do not use if you are pregnant or breastfeeding.</p>
    <div class="storage">Store in a cool, dry place out of direct sunlight. Stable for three years. Once opened, use within 12 months.</div>
  </div>
</section>

<section class="dieline dieline--front" aria-label="Front panel">
  <svg class="dieline-art" viewBox="0 0 300 530" preserveAspectRatio="none" aria-hidden="true">
    <path class="cut" d="M65 30 H115 C115 10 125 5 150 5 C175 5 185 10 185 30 H235 V278
      H258 C285 278 297 292 297 318 V445 H235 L225 445 Q222 448 222 455 V525 H175 C175 505 165 495 150 495 C135 495 125 505 125 525 H78 V455 Q78 448 75 445 H65
      H2 V318 C2 292 14 278 41 278 H65 Z"/>
    <path class="fold" d="M65 100 H235 M65 365 H235 M65 278 V445 M235 278 V445 M116 388 L118 392 H182 L184 388 M20 345 L37 362 M280 345 L263 362"/>
  </svg>
  <div class="face face--front">
    <div class="brand"><span class="brand-dot"></span>VERDAMED</div>
    <svg class="arc" viewBox="0 0 62 200" aria-hidden="true">
      <circle cx="100" cy="96" r="96" fill="var(--blue)"/>
      <circle cx="106" cy="106" r="94" fill="var(--green)"/>
    </svg>
    <h1 class="product">Cannabidiol<br>(CBD)</h1>
    <p class="spec">Self-curing adhesive<br>Polyethylene backing sheet</p>
  </div>
</section>

</body>
</html>
```